Real Estate Sign - For Sale Yard Sign - Bellwether Estates

Our real estate company is looking for a new sign design to hang from in post in the front yard of the homes we are selling. Our company name is Bellwether Estates and we are open to any ideas. Attached for you is our company logo and name. The font is Trajan Pro. We are looking for a classy sign to put in front of our high end more expensive homes. You can either choose to include or not include the words "FOR SALE" on the sign (in our state, only about 1/2 of the real estate signs have room for those words. It is implied with a sign in the yard in front of a home). Thank you.

24 inches wide is important. and the height should be either 18, 24 or 30 inches. For printing purposes either of those heights will work. 18 inches is common, but some signs look great that are taller too. I'm open.

If you have any ideas for some better text options, styles or fonts, feel free to play with it.

P.S. Please feel free to play with the colors. We are not at this point set on a particular color scheme. Colors we think are nice but you may have other better ideas are black, red, white, gold, green

Target Market(s)

High end real estate home owners who choose to use our company to sell their home.

Industry/Entity Type

Real Estate

Requirements
Must have
• Company Logo
Company Name (Bellwether Estates)
Thaddeus Vornholt (please include my name as I am the real estate agent)
503-618-2940 (my phone number for potential clients to contact me)
Website name - bellwetherestatesnw.example
***You can either choose to include the words "FOR SALE" or not***

Dimensions must be 24 inches wide. Height can be either 18, 24 or 30 inches. Must be one of those 3 heights for printing purposes.

```html
<!DOCTYPE html>
<html lang="en">
<head>
<meta charset="utf-8">
<title>Bellwether Estates – Yard Sign</title>
<link rel="stylesheet" href="https://fonts.googleapis.com/css2?family=Cinzel:wght@400;600;700&display=swap">
<style>
  :root {
    --page: #ffffff;
    --frame-tan: #d8c99c;
    --panel-black: #000000;
    --band-name: #7d7460;
    --band-phone: #575039;
    --text-white: #ffffff;
    --text-cream: #ece2c8;
    --text-band: #f1e9d4;
    --text-web: #4d4530;
  }
  html, body {
    margin: 0;
    padding: 0;
    width: 1200px;
    height: 781px;
    overflow: hidden;
    background: var(--page);
  }
  .yard-sign {
    display: block;
    width: 1200px;
    height: 781px;
  }
  .sign-text {
    font-family: "Cinzel", "Trajan Pro", serif;
    text-anchor: middle;
  }
  .brand-mark { fill: var(--frame-tan); font-size: 15px; font-weight: 600; letter-spacing: 2px; }
  .company-name { fill: var(--text-white); font-size: 48px; font-weight: 700; letter-spacing: 1px; }
  .company-tagline { fill: var(--text-cream); font-size: 30px; font-weight: 400; letter-spacing: 1px; }
  .agent-name { fill: var(--text-band); font-size: 34px; font-weight: 400; letter-spacing: 1.5px; }
  .agent-phone { fill: var(--text-band); font-size: 44px; font-weight: 400; letter-spacing: 3px; }
  .website { fill: var(--text-web); font-size: 17px; font-weight: 400; letter-spacing: 1.2px; }
</style>
</head>
<body>
<svg class="yard-sign" viewBox="0 0 1100 716" xmlns="http://www.w3.org/2000/svg" role="img" aria-label="Bellwether Estates yard sign for agent Thaddeus Vornholt">
  <defs>
    <linearGradient id="gloss" x1="0" y1="0" x2="0" y2="1">
      <stop offset="0" stop-color="#5a5a5c"/>
      <stop offset="0.55" stop-color="#3a3a3c"/>
      <stop offset="1" stop-color="#000000" stop-opacity="0"/>
    </linearGradient>
  </defs>

  <!-- frame -->
  <path class="sign-frame" fill="var(--frame-tan)"
        d="M317,158 L538,80 L760,158 L760,545 Q760,622 683,622 L394,622 Q317,622 317,545 Z"/>

  <!-- header panel -->
  <path class="header-panel" fill="var(--panel-black)"
        d="M328,168 L538,92 L749,168 L749,371 L328,371 Z"/>
  <path class="header-gloss" fill="url(#gloss)"
        d="M540,99 L741,172 L741,290 L540,290 Z"/>

  <!-- agent bands -->
  <rect class="band-name" x="328" y="371" width="421" height="80" fill="var(--band-name)"/>
  <rect class="band-phone" x="328" y="451" width="421" height="78" fill="var(--band-phone)"/>

  <!-- text -->
  <text class="sign-text brand-mark" x="538" y="165">BELLWETHER</text>
  <text class="sign-text company-name" x="540" y="274">BELLWETHER</text>
  <text class="sign-text company-tagline" x="538" y="316">Estates Real Estate</text>
  <text class="sign-text agent-name" x="538" y="423">Thaddeus Vornholt</text>
  <text class="sign-text agent-phone" x="538" y="507">503-618-2940</text>
  <text class="sign-text website" x="538" y="580">BELLWETHERESTATESNW.EXAMPLE</text>
</svg>
</body>
</html>
```